Label for packaging - front and back

Hello,
We are looking for a fresh design based off of the current one we have. We need something fresh simple and eye catching. Company is VerdanKelpa.com I am including current packaging and also a trim fold fliers we had made.
VK Brochure is what we could use as design inspiration perhaps?
Updates
PLEASE replace super food with " Past Mighty Greens". somewhere on the label. In addition, please include website name on front.
Target Market(s)
Nutrition, athletes, anyone who wants to improve health
Look and feel
Each slider illustrates characteristics of the customer's brand and the style your logo design should communicate.

```html
<!DOCTYPE html>
<html lang="en">
<head>
<meta charset="utf-8">
<title>Verdan Kelpa – Spirulina Platensis Label</title>
<link rel="stylesheet" href="https://fonts.googleapis.com/css2?family=Montserrat:wght@300;400;600;700;800&family=Satisfy&family=Carlito&display=swap">
<style>
  :root {
    --backdrop: #424242;
    --paper: #ffffff;
    --leaf-green: #6a9a3a;
    --title-green: #5f9435;
    --navy: #1d2a44;
    --teal: #3fb3a8;
    --powder-dark: #3f8f35;
    --powder-light: #77b75e;
    --bowl: #e9efe6;
  }
  * { margin: 0; padding: 0; box-sizing: border-box; }
  html, body { width: 1074px; height: 1200px; overflow: hidden; background: var(--backdrop); }
  .label {
    position: absolute; left: 240px; top: 173px; width: 595px; height: 854px;
    background: var(--paper); font-family: "Montserrat", sans-serif;
  }
  .brand {
    position: absolute; left: 176px; top: 60px; display: flex; align-items: center; gap: 14px;
  }
  .brand-dot { width: 56px; height: 56px; border-radius: 50%; background: var(--teal); }
  .brand-name {
    color: var(--navy); font-weight: 400; font-size: 21px; line-height: 1.15; letter-spacing: 3px;
  }
  .product-title {
    position: absolute; left: 0; width: 100%; top: 150px; text-align: center;
    font-family: "Satisfy", cursive; color: var(--title-green); font-size: 118px; line-height: 1;
    padding-left: 10px;
  }
  .product-species {
    position: absolute; left: 0; width: 100%; top: 265px; text-align: center; padding-left: 45px;
    color: var(--title-green); font-weight: 300; font-size: 44px; line-height: 1;
  }
  .title-rule {
    position: absolute; left: 194px; width: 206px; top: 320px; height: 1px; background: var(--title-green);
  }
  .process {
    position: absolute; left: 0; width: 100%; top: 327px; text-align: center; padding-left: 10px;
    color: var(--title-green); font-weight: 700; font-size: 21px; letter-spacing: 2.5px; line-height: 1.05;
  }
  .process small { display: block; font-size: 12.5px; letter-spacing: 0.4px; }
  .product-photo {
    position: absolute; left: 0; top: 382px; width: 100%; height: 260px;
    background: radial-gradient(ellipse 46% 80% at 50% 100%, var(--powder-light) 0%, var(--powder-dark) 58%, var(--bowl) 66%, #f7f7f5 80%, var(--paper) 100%);
  }
  .info-band {
    position: absolute; left: 0; top: 653px; width: 100%; height: 201px; background: var(--leaf-green); color: #fff;
  }
  .tagline {
    position: absolute; top: 10px; width: 100%; text-align: center; font-weight: 700; font-size: 21px;
  }
  .band-rule { position: absolute; left: 31px; width: 533px; height: 1px; background: rgba(255,255,255,.75); }
  .band-rule.top { top: 44px; }
  .band-rule.bottom { top: 325px; top: 325px; }
  .divider { position: absolute; top: 50px; width: 1px; height: 95px; background: rgba(255,255,255,.8); }
  .highlights { position: absolute; left: 39px; top: 59px; list-style: none; }
  .highlights li {
    display: flex; align-items: center; gap: 5px; height: 29.5px;
    font-weight: 700; font-size: 12.5px; letter-spacing: .2px;
  }
  .benefit { position: absolute; display: flex; align-items: center; gap: 9px; }
  .benefit-icon { width: 40px; height: 40px; flex: none; }
  .benefit p { font-family: "Carlito", sans-serif; font-size: 10.5px; line-height: 1.05; width: 112px; }
  .footer-line {
    position: absolute; top: 159px; font-size: 12.5px; font-weight: 400;
  }
</style>
</head>
<body>
<main class="label">
  <div class="brand">
    <span class="brand-dot"></span>
    <div class="brand-name">VERDAN<br>KELPA</div>
  </div>

  <h1 class="product-title">Spirulina</h1>
  <p class="product-species">Platensis</p>
  <div class="title-rule"></div>
  <p class="process">FREEZE DRIED<small>TO PRESERVE ALL NUTRITION</small></p>

  <div class="product-photo" role="img" aria-label="Photo of green spirulina powder in a pale ceramic bowl"></div>

  <section class="info-band">
    <h2 class="tagline">Past Mighty Greens</h2>
    <div class="band-rule top"></div>

    <ul class="highlights">
      <li><svg width="20" height="20" viewBox="0 0 20 20"><circle cx="9" cy="11" r="8" fill="none" stroke="#fff" stroke-width="1.6"/><path d="M5 11l4 4 9-11" fill="none" stroke="#fff" stroke-width="2"/></svg>PROTIN 70%</li>
      <li><svg width="20" height="20" viewBox="0 0 20 20"><circle cx="9" cy="11" r="8" fill="none" stroke="#fff" stroke-width="1.6"/><path d="M5 11l4 4 9-11" fill="none" stroke="#fff" stroke-width="2"/></svg>AMINO ACID19</li>
      <li><svg width="20" height="20" viewBox="0 0 20 20"><circle cx="9" cy="11" r="8" fill="none" stroke="#fff" stroke-width="1.6"/><path d="M5 11l4 4 9-11" fill="none" stroke="#fff" stroke-width="2"/></svg>VITAMINS</li>
    </ul>

    <div class="divider" style="left:198px"></div>
    <div class="divider" style="left:396px"></div>

    <div class="benefit" style="left:222px;top:55px">
      <svg class="benefit-icon" viewBox="0 0 40 40"><circle cx="20" cy="20" r="20" fill="#fff"/><g stroke="#6a9a3a" stroke-width="2"><path d="M12 13l8 7 9-6M20 20l-8 7M20 20l8 7"/></g><g fill="#6a9a3a"><circle cx="20" cy="20" r="4"/><circle cx="12" cy="13" r="3"/><circle cx="29" cy="14" r="3"/><circle cx="12" cy="27" r="3"/><circle cx="28" cy="27" r="3"/></g></svg>
      <p>Excellent source of zinc to boost your immune system.</p>
    </div>
    <div class="benefit" style="left:222px;top:103px">
      <svg class="benefit-icon" viewBox="0 0 40 40"><circle cx="20" cy="20" r="20" fill="#fff"/><path d="M11 30c-2-7 0-14 4-18l4 2-2 4 2 2c5-3 10-1 11 4s-3 7-8 6z" fill="#6a9a3a"/></svg>
      <p>Vitamins B1, B2, B3, B5, B6, B7, B8, B9, C, D, E and K.</p>
    </div>
    <div class="benefit" style="left:420px;top:55px">
      <svg class="benefit-icon" viewBox="0 0 40 40"><circle cx="20" cy="20" r="20" fill="#fff"/><path d="M11 29c0-10 7-17 18-18 0 11-7 17-16 17z" fill="#6a9a3a"/><path d="M10 31l14-14" stroke="#fff" stroke-width="1.4"/></svg>
      <p>Rich in chlorophyll</p>
    </div>
    <div class="benefit" style="left:420px;top:103px">
      <svg class="benefit-icon" viewBox="0 0 40 40"><circle cx="20" cy="20" r="20" fill="#fff"/><path d="M20 30l-9-9a5 5 0 0 1 9-6 5 5 0 0 1 9 6z" fill="none" stroke="#6a9a3a" stroke-width="2.2"/><path d="M12 21h5l2-4 3 7 2-3h4" fill="none" stroke="#6a9a3a" stroke-width="1.6"/></svg>
      <p>Powerful source of antioxidants and protein</p>
    </div>

    <div class="band-rule" style="top:152px"></div>
    <p class="footer-line" style="left:41px">www.VerdanKelpa.com</p>
    <p class="footer-line" style="right:41px">Net Weight:&nbsp; 120g</p>
  </section>
</main>
</body>
</html>
```